Trendora - Forex Signal Services Moment is All. Shape your path.

I need an attractive eye catching web design that is azure friendly. I currently have a web programmer working on the backend of my website. Now I need a professional design to attract and retain customers. This site needs to be mobile friendly.

Trendora is a highly reputable, trustworthy and professional site that offers forex signals to traders in all parts of the globe. With accurate and reliable forex signals, traders can not only make money but also boost their profits.

At Trendora, we want our clients to have complete faith on us and our services! We also do not want our users to lead a simple and monotonous life. Instead our goal is to help them create an extra source of steady income. However, this is possible only when our clients resolve to change their lives for the better. They need to change their mindset and most importantly develop a positive frame of mind. That’s exactly why at Trendora, we provide our clients with innumerable personal development tools and resources that’ll aid them in changing all the aspects of their lives. We want our traders to feel inspired and educate them in the right way!

Colors are flexible.

I do like the simplicity of www.bluemarrowtrade.example.
I do want a design more professional in appearance and not everything on page one.

I have not been able to decide on a logo. There is one of lower quality as I have not paid for it yet but I will if you decide it's the best for my business I will. Or should one feel that they have a better idea for a logo, I will pay for it if i like it.

I have included some of the content of my site so you can get a feel for where I am coming from.
(Please note that this content is still in the editing process)

Project Deadline Extended Reason: My content was not complete nor finalization of the final logo. We will allow a few more days for designers to modify the website.Thank you for your patience and understanding. Added Tuesday, January 24, 2017

Target Market(s)

I work with Forex Traders, Investors wanting to control their own portfolios, and remote nomads/mellienials

Coding

Coded - Design and coding required

Number of Pages Required

5+ page

Requirements
Must have
• I must have a professional clean look. I want the site to be interactive and eye catching. I want my audience hooked within seconds of opening it. It has to have all important information first. Photos must be legit and not spammy. I work as a representative in the financial market. I want my site to reflect that I stand by my product and reputation means everything to me. This site has to be engaging.
• Sorry, I should have included this earlier of what I will all need on this site.
• I'll have about Trendora (my company, what we stand for, who we work with, my strategy, etc....
• about me (why i started this company, who I am)
• Performance (graphs and recent posts of signals)
• Membership (how to sign up)
• Terms of service/legal/disclaimers
• FAQS
• Personal Development Resources
• Forex Education Resources
Nice to have
• Quick links to bounce around the site faster.
Should not have
• I do not want over the top white collar conservative.

```html
<!DOCTYPE html>
<html lang="en">
<head>
<meta charset="utf-8">
<title>Trendora - Forex Signal Services</title>
<link href="https://fonts.googleapis.com/css2?family=Open+Sans:wght@400;600;700&display=swap" rel="stylesheet">
<style>
:root{
  --green:#a3c83a;
  --green-dark:#8db02a;
  --ink:#1b1f29;
  --black:#000;
  --white:#fff;
  --grey:#e1e1e1;
  --text:#222;
  --muted:#cfd3da;
}
*{box-sizing:border-box;margin:0;padding:0}
html,body{width:1200px;height:3689px;overflow:hidden}
body{position:relative;background:var(--white);font-family:"Open Sans",sans-serif;color:var(--text)}
.abs{position:absolute}
.topbar{left:0;top:0;width:1200px;height:88px;background:var(--ink)}
.brand{color:var(--green);font-weight:700;font-size:40px;line-height:1;letter-spacing:-1px}
.brand-tag{color:var(--green);font-size:9px;font-weight:700;letter-spacing:2px}
.contact{color:var(--muted);font-size:12px;display:flex;align-items:center;gap:8px;top:32px}
.contact svg{fill:var(--green)}
.social-dot{width:18px;height:18px;border-radius:50%;background:var(--green);top:33px}
.nav{left:0;top:88px;width:1200px;height:32px;background:var(--green)}
.nav span{position:absolute;top:7px;font-size:13px;color:var(--ink);font-weight:600}
.hero{left:0;top:120px;width:1200px;height:556px;background:linear-gradient(110deg,#7a6f57 0%,#5b5648 40%,#2c3a44 70%,#4a4f4a 100%)}
.hero-title{left:0;width:1200px;top:285px;text-align:center;color:var(--white);font-weight:700;font-size:36px;line-height:42px;letter-spacing:3px}
.hero-copy{left:250px;width:700px;top:390px;text-align:center;color:#e4e4e4;font-size:15px;line-height:21px}
.btn{background:var(--green);color:var(--ink);font-size:15px;font-weight:600;text-align:center;display:flex;align-items:center;justify-content:center;border-radius:2px}
.dot{width:12px;height:12px;border-radius:50%;background:var(--green);top:651px}
.heading{width:222px;height:67px;border:3px solid var(--green);display:flex;align-items:center;justify-content:center;font-weight:700;font-size:24px;color:var(--ink);letter-spacing:1px;background:var(--white)}
.service{width:300px;text-align:center}
.service-ring{width:138px;height:138px;border-radius:50%;background:var(--green);margin:0 auto;display:flex;align-items:center;justify-content:center}
.service-core{width:106px;height:106px;border-radius:50%;background:var(--black);border:6px solid var(--green);outline:4px solid var(--black);display:flex;align-items:center;justify-content:center}
.service h3{font-size:14px;font-weight:700;margin-top:22px;color:var(--black)}
.service p{font-size:13px;line-height:17px;margin-top:6px;color:var(--black)}
.photo{background:linear-gradient(135deg,#c9d3dc,#7d8894 55%,#3a4350)}
.about-copy{left:630px;top:1400px;width:482px;font-size:13px;line-height:20px;color:var(--black)}
.band{left:0;top:1736px;width:1200px;height:204px;background:linear-gradient(90deg,#6f6a66,#b49a86 40%,#8696a9 70%,#5b6a80)}
.band-title{left:0;width:1200px;top:1820px;text-align:center;font-size:28px;font-weight:700;color:var(--ink)}
.plan{width:330px;height:251px;border:2px solid var(--ink);top:1999px;border-radius:3px;overflow:hidden}
.plan-head{height:31px;background:var(--black);color:var(--white);font-weight:700;font-size:17px;text-align:center;line-height:31px}
.plan-price{height:30px;background:var(--black);border-top:2px solid var(--green);color:var(--green);font-size:13px;font-weight:700;text-align:center;line-height:28px}
.plan p{font-size:13px;line-height:17px;margin:18px 14px 0;color:var(--black)}
.plan .btn{position:absolute;left:92px;bottom:30px;width:142px;height:34px;font-size:14px}
.perf-panel{left:595px;top:2503px;width:519px;height:352px;border:2px solid #444}
.select{height:24px;background:var(--black);color:var(--white);font-size:12px;padding-left:6px;line-height:24px}
.select::after{content:"▴▾";position:absolute;right:6px;top:0;font-size:8px;letter-spacing:-1px}
.field{background:var(--grey);font-size:13px;color:#333;padding:6px 6px}
.footer{left:0;top:3425px;width:1200px;height:264px;background:var(--ink);color:var(--white)}
.foot-item{color:var(--white);font-size:14px;display:flex;align-items:center;gap:14px}
.foot-links{left:413px;top:3470px;font-size:15px;display:flex;gap:16px}
.foot-title{font-size:15px;font-weight:600}
.foot-social{width:30px;height:30px;border-radius:50%;border:3px solid var(--white);top:3514px}
.newsletter{left:829px;top:3598px;width:233px;height:51px;background:var(--white);color:#555;font-size:12px;font-style:italic;padding:17px 10px}
.go{left:1062px;top:3598px;width:57px;height:51px;background:#2bc4d8;color:var(--white);font-weight:700;font-size:15px;display:flex;align-items:center;justify-content:center}
</style>
</head>
<body>

<header class="abs topbar">
  <div class="abs" style="left:86px;top:12px">
    <div class="brand">Trendora</div>
    <div class="brand-tag" style="margin-top:4px">SHAPE YOUR PATH</div>
  </div>
  <div class="abs contact" style="left:300px"><svg width="14" height="18" viewBox="0 0 14 18"><path d="M7 0a7 7 0 0 0-7 7c0 5 7 11 7 11s7-6 7-11a7 7 0 0 0-7-7zm0 10a3 3 0 1 1 0-6 3 3 0 0 1 0 6z"/></svg>418 Harbor Lane, NY</div>
  <div class="abs contact" style="left:472px"><svg width="20" height="14" viewBox="0 0 20 14"><path d="M0 0h20v14H0z"/><path d="M0 0l10 8 10-8" stroke="#1b1f29" stroke-width="1.6" fill="none"/></svg>hello@trendora.example</div>
  <div class="abs contact" style="left:702px"><svg width="16" height="16" viewBox="0 0 16 16"><path d="M3 0l3 4-2 2c1 2 4 5 6 6l2-2 4 3-2 3C7 16 0 9 0 3z"/></svg>+92 5550147732</div>
  <div class="abs contact" style="left:905px"><svg width="16" height="16" viewBox="0 0 16 16"><circle cx="8" cy="8" r="8"/><path d="M8 3v5h4" stroke="#1b1f29" stroke-width="1.8" fill="none"/></svg>9:00 - 18:00</div>
  <div class="abs social-dot" style="left:1035px"></div>
  <div class="abs social-dot" style="left:1075px"></div>
  <div class="abs social-dot" style="left:1115px"></div>
</header>

<nav class="abs nav">
  <span style="left:86px">MENU ▾</span>
  <span style="left:214px">ABOUT ME</span>
  <span style="left:374px">PERFORMANCE</span>
  <span style="left:561px">MEMBERSHIP</span>
  <span style="left:738px">FAQS</span>
  <span style="left:1003px">LOGIN / SIGN UP</span>
</nav>

<section>
  <div class="abs hero" role="img" aria-label="Desk with a phone and a tablet showing a forex price chart"></div>
  <h1 class="abs hero-title">WELCOME TO<br>TRENDORA</h1>
  <p class="abs hero-copy">We use proven strategies to help traders in succeeding in the forex market. Our forex experts provide high-probability, professional and consistent forex signals and charts that help traders in maximizing their profits and eliminating losses.</p>
  <div class="abs btn" style="left:529px;top:480px;width:142px;height:34px">Read more</div>
  <div class="abs dot" style="left:539px;background:var(--white)"></div>
  <div class="abs dot" style="left:565px"></div>
  <div class="abs dot" style="left:591px"></div>
  <div class="abs dot" style="left:617px"></div>
  <div class="abs dot" style="left:643px"></div>
</section>

<section>
  <h2 class="abs heading" style="left:489px;top:755px">SERVICES</h2>

  <div class="abs service" style="left:120px;top:885px">
    <div class="service-ring"><div class="service-core">
      <svg width="44" height="44" viewBox="0 0 44 44" fill="none" stroke="#a3c83a" stroke-width="3"><circle cx="22" cy="22" r="7"/><path d="M22 4v7M22 33v7M4 22h7M33 22h7M9 9l5 5M30 30l5 5M35 9l-5 5M14 30l-5 5"/></svg>
    </div></div>
    <h3>The BlueMarrowFX Advantage</h3>
    <p>You have to know your game in order<br>to profit from the Forex Market. Everything<br>you learn about the box and every<br>time you practice what you have learnt – you gain</p>
    <div class="btn" style="width:142px;height:34px;margin:12px auto 0">Read more</div>
  </div>

  <div class="abs service" style="left:450px;top:885px">
    <div class="service-ring"><div class="service-core">
      <svg width="44" height="44" viewBox="0 0 44 44" fill="#a3c83a"><path d="M4 4h36v36H4z" fill="none" stroke="#a3c83a" stroke-width="3"/><rect x="11" y="24" width="5" height="11"/><rect x="19" y="18" width="5" height="17"/><rect x="27" y="12" width="5" height="23"/></svg>
    </div></div>
    <h3>The BlueMarrowFX Advantage</h3>
    <p>You have to know your game in order<br>to profit from the Forex Market. Everything<br>you learn about the box and every<br>time you practice what you have learnt – you gain</p>
    <div class="btn" style="width:142px;height:34px;margin:12px auto 0">Read more</div>
  </div>

  <div class="abs service" style="left:780px;top:885px">
    <div class="service-ring"><div class="service-core">
      <svg width="44" height="44" viewBox="0 0 44 44"><path d="M22 4h18v36H22" fill="none" stroke="#a3c83a" stroke-width="3"/><path d="M4 17h14v-8l12 13-12 13v-8H4z" fill="#a3c83a"/></svg>
    </div></div>
    <h3>The BlueMarrowFX Advantage</h3>
    <p>You have to know your game in order<br>to profit from the Forex Market. Everything<br>you learn about the box and every<br>time you practice what you have learnt – you gain</p>
    <div class="btn" style="width:142px;height:34px;margin:12px auto 0">Read more</div>
  </div>
</section>

<section>
  <div class="abs photo" style="left:86px;top:1296px;width:509px;height:337px" role="img" aria-label="Business team meeting around a table with laptops"></div>
  <h2 class="abs heading" style="left:630px;top:1296px">WHO WE ARE</h2>
  <p class="abs about-copy">Pardon my language but there is a lot of 'crap', on the internet, especially when it comes to the services I offer. I have spent countless hours and years of my life towards my passion for the currency industry. I finally developed a strategy I am proud of and stand by my product with my name and company brand. I wholeheartedly believe that the extent of our personal success is a measure of accomplishments we have helped others create.I want people to succeed. I am a forex day trader AND life coach. I believe our lives are a journey. I believe that one should live their passion. Otherwise, what's the point.</p>
  <div class="abs btn" style="left:630px;top:1576px;width:142px;height:33px">Read more</div>
</section>

<section>
  <div class="abs band" role="img" aria-label="Team members stacking hands together"></div>
  <h2 class="abs band-title">MEMBERSHIP</h2>

  <div class="abs plan" style="left:86px">
    <div class="plan-head">1 MONTH</div>
    <div class="plan-price">Rs. 15000.00</div>
    <p>My life mission is to grow, teach and apply what I've learnt to my future</p>
    <div class="btn">Order now</div>
  </div>
  <div class="abs plan" style="left:435px">
    <div class="plan-head">3 MONTHS</div>
    <div class="plan-price">Rs. 40000.00</div>
    <p>My life mission is to grow, teach and apply what I've learnt to my future</p>
    <div class="btn">Order now</div>
  </div>
  <div class="abs plan" style="left:784px">
    <div class="plan-head">12 MONTHS</div>
    <div class="plan-price">Rs. 80000.00</div>
    <p>My life mission is to grow, teach and apply what I've learnt to my future</p>
    <div class="btn">Order now</div>
  </div>
</section>

<section>
  <h2 class="abs heading" style="left:489px;top:2368px">PERFORMANCE</h2>
  <div class="abs photo" style="left:86px;top:2503px;width:509px;height:352px;background:linear-gradient(135deg,#5d7fa6,#c9d6e2 45%,#eef2f5 70%,#9fb1c4)" role="img" aria-label="Hands pointing a pen at printed bar charts"></div>
  <div class="abs perf-panel"></div>
  <div class="abs select" style="left:632px;top:2516px;width:98px">MARCH</div>
  <div class="abs select" style="left:979px;top:2516px;width:98px">2016</div>
</section>

<section>
  <h2 class="abs heading" style="left:489px;top:2970px">FAQ</h2>
  <div class="abs field" style="left:111px;top:3101px;width:435px;height:37px;padding-top:10px">Name</div>
  <div class="abs field" style="left:595px;top:3101px;width:492px;height:37px;padding-top:10px">Email</div>
  <div class="abs field" style="left:111px;top:3160px;width:578px;height:179px">Message...........</div>
  <div class="abs btn" style="left:944px;top:3307px;width:143px;height:35px;font-size:14px">Submit</div>
</section>

<footer class="abs footer">
  <div class="abs" style="left:86px;top:28px">
    <div class="brand" style="font-size:32px">Trendora</div>
    <div class="brand-tag" style="font-size:7px;margin-top:2px">SHAPE YOUR PATH</div>
  </div>
  <div class="abs foot-item" style="left:86px;top:96px">
    <svg width="20" height="26" viewBox="0 0 14 18" fill="none" stroke="#fff" stroke-width="1.4"><path d="M7 1a6 6 0 0 0-6 6c0 4.5 6 10 6 10s6-5.5 6-10a6 6 0 0 0-6-6z"/><circle cx="7" cy="7" r="2.2"/></svg>
    <span style="line-height:20px">Ravel Street 4/12<br>city centre, Eastmoor</span>
  </div>
  <div class="abs foot-item" style="left:86px;top:162px">
    <svg width="22" height="22" viewBox="0 0 16 16" fill="#fff"><path d="M3 0l3 4-2 2c1 2 4 5 6 6l2-2 4 3-2 3C7 16 0 9 0 3z"/></svg>05550198844
  </div>
  <div class="abs foot-item" style="left:86px;top:214px">
    <svg width="24" height="17" viewBox="0 0 20 14"><rect width="20" height="14" fill="#fff"/><path d="M0 0l10 8 10-8" stroke="#1b1f29" stroke-width="1.6" fill="none"/></svg>info@trendora.example
  </div>
  <div class="abs foot-links" style="top:45px">
    <span>Trendora</span><span>About me</span><span>Performance</span><span>Membership</span><span>Faq's</span>
  </div>
  <div class="abs foot-title" style="left:413px;top:165px">Useful Links</div>
  <div class="abs foot-title" style="left:829px;top:45px">Follow us</div>
</footer>
<div class="abs foot-social" style="left:832px"></div>
<div class="abs foot-social" style="left:894px"></div>
<div class="abs foot-social" style="left:956px"></div>
<div class="abs foot-social" style="left:1018px"></div>
<div class="abs newsletter">Enter your email</div>
<div class="abs go">Go</div>

</body>
</html>
```